Business Card Design Project

Our slogan is "dare to be different" and we are after something creative and different to go with our company image.

Criteria:
The business card will not be a standard size but it must be small or big enough to fit in a wallet.
It will be double sided
It will have our colours and the design will be based around our logo (attached)
No fancy text just clean sharp easy to read. we have been using the stag sans book font type so this or similar type is preferable (we are not locked in a font type.

For more information about us, please visit out website at www.tovelmarsh.com.au

Target Market(s)

outdoor and recreational industry/market

Industry/Entity Type

Business

Requirements
Must have
• Logo
Slogan
website
contact details (phone and email)
Name and Position
social media facebook and youtube

```html
<!DOCTYPE html>
<html lang="en">
<head>
<meta charset="utf-8">
<title>Tovelmarsh Business Card – Actual Size</title>
<link rel="stylesheet" href="https://fonts.googleapis.com/css2?family=Questrial&family=Archivo:ital,wght@0,500;0,600;0,700;1,500&family=Roboto+Mono:wght@500&display=swap">
<style>
  :root {
    --sheet: #ffffff;
    --ink: #111111;
    --card: #29292b;
    --accent: #dd2a0a;
    --paper-text: #ffffff;
  }
  html, body {
    margin: 0;
    padding: 0;
    width: 1200px;
    height: 846px;
    overflow: hidden;
    background: var(--sheet);
  }
  .sheet {
    position: relative;
    width: 1200px;
    height: 846px;
    font-family: "Archivo", Arial, sans-serif;
    color: var(--ink);
  }
  .dimension-line { position: absolute; background: var(--ink); }
  .dimension-line--width { left: 95px; top: 213px; width: 514px; height: 2px; }
  .dimension-line--height { left: 77px; top: 239px; width: 2px; height: 285px; }
  .dimension-label {
    position: absolute;
    font-weight: 700;
    font-size: 20px;
    line-height: 1;
  }
  .dimension-label--width { left: 315px; top: 183px; }
  .dimension-label--height { left: 18px; top: 379px; }

  .card {
    position: absolute;
    top: 233px;
    width: 509px;
    height: 290px;
    background: var(--card);
    color: var(--paper-text);
    overflow: hidden;
  }
  .card--back { left: 95px; }
  .card--front { left: 652px; width: 508px; }
  .card svg { position: absolute; left: 0; top: 0; }

  .side-label {
    position: absolute;
    top: 557px;
    font-weight: 700;
    font-size: 13px;
    letter-spacing: 5px;
    line-height: 1;
  }
  .side-label--back { left: 96px; }
  .side-label--front { left: 653px; }

  .wordmark {
    position: absolute;
    font-family: "Questrial", Arial, sans-serif;
    color: var(--paper-text);
    line-height: 1;
    white-space: nowrap;
  }
  .card--back .wordmark { right: 18px; top: 221px; font-size: 24px; letter-spacing: 0.3px; }
  .card--front .wordmark { left: 84px; top: 252px; font-size: 20px; letter-spacing: 0; }

  .web-links {
    position: absolute;
    left: 14px;
    top: 216px;
    margin: 0;
    font-family: "Roboto Mono", monospace;
    font-size: 8.2px;
    letter-spacing: 1px;
    line-height: 11px;
  }
  .slogan {
    position: absolute;
    left: 14px;
    top: 266px;
    width: 482px;
    margin: 0;
    display: flex;
    justify-content: space-between;
    font-weight: 700;
    font-size: 11px;
    line-height: 1;
  }

  .person { position: absolute; left: 83px; top: 88px; }
  .person__name {
    margin: 0;
    color: var(--accent);
    font-weight: 600;
    font-size: 15px;
    line-height: 1;
  }
  .person__position {
    margin: 4px 0 0;
    font-style: italic;
    font-weight: 500;
    font-size: 10.5px;
    line-height: 1;
  }

  .contact-divider { position: absolute; top: 247px; width: 2px; height: 32px; background: var(--paper-text); }
  .contact-divider--first { left: 232px; }
  .contact-divider--second { left: 348px; }
  .contact-list {
    position: absolute;
    top: 243px;
    margin: 0;
    padding: 0;
    list-style: none;
    font-weight: 500;
    line-height: 20px;
    font-size: 13px;
    white-space: nowrap;
  }
  .contact-list--phones { left: 244px; }
  .contact-list--other { left: 360px; }
  .contact-list__key { display: inline-block; width: 14px; font-size: 13px; }
  .contact-list__value--small { font-size: 10px; letter-spacing: -0.1px; }

  .caption {
    position: absolute;
    left: 0;
    width: 1214px;
    text-align: center;
    font-weight: 600;
    font-size: 19px;
    line-height: 1;
  }
  .caption--title { top: 739px; }
  .caption--size { top: 780px; }
</style>
</head>
<body>
<main class="sheet">
  <div class="dimension-line dimension-line--width"></div>
  <div class="dimension-label dimension-label--width">9cm</div>
  <div class="dimension-line dimension-line--height"></div>
  <div class="dimension-label dimension-label--height">5cm</div>

  <section class="card card--back" aria-label="Card back">
    <svg width="509" height="290" viewBox="0 0 509 290" aria-hidden="true">
      <polygon points="371,0 482,0 426,54" fill="var(--accent)"/>
      <circle cx="426" cy="135" r="65" fill="#18181a" stroke="var(--accent)" stroke-width="4"/>
    </svg>
    <p class="web-links">http://www.tovelmarsh.com.au/<br>www.facebook.com/TovelMarsh<br>www.youtube.com/TheTovelMarsh</p>
    <div class="wordmark">TOVELMARSH</div>
    <p class="slogan" aria-label="Dare to be different">
      <span>D</span><span>A</span><span>R</span><span>E</span><span>&nbsp;</span><span>T</span><span>O</span><span>&nbsp;</span><span>B</span><span>E</span><span>&nbsp;</span><span>D</span><span>I</span><span>F</span><span>F</span><span>E</span><span>R</span><span>E</span><span>N</span><span>T</span>
    </p>
  </section>
  <div class="side-label side-label--back">BACK</div>

  <section class="card card--front" aria-label="Card front">
    <svg width="508" height="290" viewBox="0 0 508 290" aria-hidden="true">
      <polygon points="28,0 138,0 83,55" fill="var(--accent)"/>
      <polygon points="508,235 480,263 508,290" fill="var(--accent)"/>
    </svg>
    <div class="person">
      <p class="person__name">Name</p>
      <p class="person__position">position</p>
    </div>
    <div class="wordmark">TOVELMARSH</div>
    <div class="contact-divider contact-divider--first"></div>
    <ul class="contact-list contact-list--phones">
      <li><span class="contact-list__key">M</span>0123456789</li>
      <li><span class="contact-list__key">O</span>0123456789</li>
    </ul>
    <div class="contact-divider contact-divider--second"></div>
    <ul class="contact-list contact-list--other">
      <li><span class="contact-list__key">F</span>0123456789</li>
      <li><span class="contact-list__key">E</span><span class="contact-list__value--small">email@tovelmarsh.com</span></li>
    </ul>
  </section>
  <div class="side-label side-label--front">FRONT</div>

  <div class="caption caption--title">Business card</div>
  <div class="caption caption--size">Actual size</div>
</main>
</body>
</html>
```